Tidal Puffs. the aim is to sell vaping liquids based on mood or feelings

We are a company who sell vaping liquids. A designer from this site created a good logo for our company. I now need to use this logo and create a label to place onto vaping bottles. Unusually we will be selling vaping products based on Moods rather than flavours.

To be clear therefore the label should have our company Logo but then also reflect a particular type of Mood or feeling.

The designs for the various moods will then be printed as labels for our vaping bottles. We have 9 different Tidal Puffs (see below) that we intend to bring to the market and general public

i would therfore like designs for the following 9 feelings/moods:

Love
Chilled
Happy
Energy
Desire
Bliss
Lust
Calm
High

the first attachment has our stand alone Logo.

i will then send some attachments of ideas we were playing around with to point you in the right direction. i will need the designs to be very colourful and to reflect the mood.

i do like the love hart one so it doesn't necessarily mean that we need to have images of people on the label. i will leave it to the designers to use images they feel best reflects the specific mood

Target Market(s)

General public

Industry/Entity Type

Retail

Colors

Designer to choose colors to be used in the design.

Requirements
Must have
• my company logo on any design
Nice to have
• vibrant colours or image to match the particular mood vape

```html
<!DOCTYPE html>
<html lang="en">
<head>
<meta charset="UTF-8">
<title>Tidal Puffs – Love Label</title>
<link rel="stylesheet" href="https://fonts.googleapis.com/css2?family=Montserrat:wght@400;700&display=swap">
<style>
  :root {
    --magenta: #e23be6;
    --pink: #f7a6e6;
    --blush: #fbd3e8;
    --peach: #f9c7b8;
    --white: #ffffff;
    --plum: #6b1a78;
    --love-red: #e8141c;
  }
  html, body {
    margin: 0;
    padding: 0;
    width: 1200px;
    height: 903px;
    overflow: hidden;
    background: var(--white);
  }
  .label {
    position: relative;
    width: 1200px;
    height: 903px;
    overflow: hidden;
    font-family: "Montserrat", Arial, sans-serif;
  }
  .mood-backdrop {
    position: absolute;
    inset: 0;
    background:
      radial-gradient(circle at 12% 20%, var(--magenta) 0, transparent 18%),
      radial-gradient(circle at 88% 15%, var(--magenta) 0, transparent 16%),
      radial-gradient(circle at 95% 60%, var(--white) 0, transparent 18%),
      radial-gradient(circle at 5% 65%, var(--white) 0, transparent 16%),
      radial-gradient(circle at 30% 75%, var(--magenta) 0, transparent 14%),
      radial-gradient(circle at 78% 78%, var(--magenta) 0, transparent 15%),
      radial-gradient(circle at 55% 5%, var(--peach) 0, transparent 20%),
      radial-gradient(circle at 20% 45%, var(--pink) 0, transparent 22%),
      linear-gradient(135deg, var(--blush) 0%, var(--pink) 40%, var(--blush) 70%, var(--peach) 100%);
  }
  .logo-badge {
    position: absolute;
    left: 301px;
    top: 101px;
    width: 600px;
    height: 600px;
    box-sizing: border-box;
    border-radius: 50%;
    background: var(--white);
    border: 10px solid var(--plum);
    display: flex;
    align-items: center;
    justify-content: center;
  }
  .brand-name {
    margin: 0;
    font-weight: 700;
    font-size: 82px;
    color: var(--plum);
    letter-spacing: 1px;
    text-align: center;
    line-height: 1;
  }
  .mood-band {
    position: absolute;
    left: 0;
    top: 718px;
    width: 1200px;
    height: 110px;
    box-sizing: border-box;
    background: var(--white);
    border-top: 8px solid var(--plum);
    border-bottom: 8px solid var(--plum);
    display: flex;
    align-items: center;
    justify-content: center;
  }
  .mood-name {
    margin: 0;
    font-weight: 400;
    font-size: 92px;
    line-height: 1;
    color: var(--love-red);
    letter-spacing: 0.85em;
    padding-left: 0.85em;
  }
</style>
</head>
<body>
  <main class="label">
    <div class="mood-backdrop" role="img" aria-label="Soft blurred pink, magenta and white abstract mood background"></div>
    <div class="logo-badge">
      <p class="brand-name">Tidal Puffs</p>
    </div>
    <div class="mood-band">
      <h1 class="mood-name">LOVE</h1>
    </div>
  </main>
</body>
</html>
```